Medical Marihuana Ziplock Bag Mockup Design

We seek skilled and professional designer for medical marihuana ziplock bag packaging design. We need a modern, minimal, clean Design with the name productname: Plorix - Endproduct will be a ziplock bag (see attachment) samples.
Product may but must not contain a cannabis leaf in Design7Logo

Target Market(s)

young audience

Industry/Entity Type

Medical

Logo Text

P L O R X

Font styles to use
Serif
Sans Serif

Colors
9bcb3c
abd037
cadf82
ffc214
fece3e
fee18a
6b449b
886aae
b8a6cd

Requirements
Nice to have
• Can but must not contain a minimal cannabis leaf as abstract sign

```html
<!DOCTYPE html>
<html lang="en">
<head>
<meta charset="UTF-8">
<title>Plorix – Ziplock Bag Label</title>
<link rel="stylesheet" href="https://fonts.googleapis.com/css2?family=Quicksand:wght@400;500;700&display=swap">
<style>
  :root {
    --backdrop: #e6e6e9;
    --label-white: #f7f7f7;
    --brand-purple: #6b449b;
    --purple-rule: #b8a6cd;
    --leaf-green: #9bcb3c;
    --ink-dark: #3c3c42;
    --text-light: #ffffff;
  }
  * { margin: 0; padding: 0; box-sizing: border-box; }
  html, body {
    width: 729px;
    height: 1200px;
    overflow: hidden;
    background: var(--backdrop);
    font-family: "Quicksand", sans-serif;
  }
  .canvas {
    position: relative;
    width: 729px;
    height: 1200px;
  }
  .label {
    position: absolute;
    left: 142px;
    top: 206px;
    width: 445px;
    height: 784px;
  }
  .label-shape {
    position: absolute;
    inset: 0;
    width: 445px;
    height: 784px;
  }
  .label-header {
    position: absolute;
    left: 0;
    top: 0;
    width: 445px;
    height: 284px;
    display: flex;
    align-items: flex-end;
    justify-content: center;
    padding-bottom: 30px;
  }
  .brand-name {
    font-weight: 400;
    font-size: 74px;
    line-height: 1;
    color: var(--ink-dark);
    text-transform: lowercase;
    letter-spacing: 1px;
  }
  .rule {
    position: absolute;
    left: 91px;
    width: 263px;
    height: 2px;
    background: var(--purple-rule);
  }
  .rule-top { top: 340px; }
  .rule-bottom { top: 614px; }
  .product-copy {
    position: absolute;
    left: 40px;
    top: 356px;
    width: 365px;
    height: 244px;
    display: flex;
    align-items: center;
    justify-content: center;
    text-align: center;
    font-weight: 500;
    font-size: 21.5px;
    line-height: 1.44;
    color: var(--text-light);
  }
  .net-weight {
    position: absolute;
    left: 0;
    top: 668px;
    width: 445px;
    text-align: center;
    font-weight: 700;
    font-size: 32px;
    color: var(--text-light);
  }
</style>
</head>
<body>
<main class="canvas">
  <section class="label">
    <svg class="label-shape" viewBox="0 0 445 784" aria-hidden="true">
      <rect class="header-panel" x="0" y="0" width="445" height="284" fill="var(--label-white)"/>
      <polygon class="info-panel" points="0,284 445,284 445,720 222.5,768 0,720" fill="var(--brand-purple)"/>
      <polygon class="chevron-band" points="0,720 222.5,768 445,720 445,736 222.5,784 0,736" fill="var(--leaf-green)"/>
    </svg>

    <header class="label-header">
      <h1 class="brand-name">Plorix</h1>
    </header>

    <div class="rule rule-top"></div>
    <p class="product-copy">Mauris gravida elit porttitor laoreet luctus. In hac habitasse platea dictumst. Aenean leo mi, tempor ut purus in, tincidunt accumsan odio. Cras viverra lorem in metus luctus porttitor.</p>
    <div class="rule rule-bottom"></div>

    <p class="net-weight">10g</p>
  </section>
</main>
</body>
</html>
```